Verdant Row

Currently www.verdantrow-example.com. This site was designed with a generic templet. However it is functional. I'm looking for a fun, fresh, and professional design. I also need help getting the XML for Searchly and Findo. I'm not a web designer and need help. I do not like my current sites narrow width.
Updates

All and all I'm liking the designs. The earlier ones seem better. Some seem that they are just taking my images and inputing them into a templet. I could have done that. The pictures are nice. Please keep in mind, functionality and updates. Please help us show our customers our how we are different. Safe Reliable Responsible are the key fundamentals, inside of these fundamentals show that were are customer service specialized. We are, Licensed, Insured, Drug Screened, Criminally Screened. Seems that people are putting up nice pictures but not capturing our values. Please help us market us on our website. Show our prospective customers why we are better, how we differentiate ourself from the competitors. Why choose us? Our flyers and cards are designed to drive our prospective customers to the website. If it looks identical with no pazaz like the card, then the marketing chain failed. I included our cards to help guide the thought process of our company. The link below is a feature I would love to have. This may be another project itself. I'm not sure if PX is the place to accomplish it. Below is a link for people to estimate there lawns with globe viewer. I would like to give a range of estimates using this technology. I have no clue how to accomplish it. If anyone knows how to who could do this, Please let me know. https://www.yardquoter-example.com/showOrder/MOWLAWN/propertyDetails

Target Market(s)

We target residential customers 30-80 yr old. We also are expanding and placing a special emphasis on Business accounts. The main service is a mowing and landscape maintenance. Should be the main focus of the site.

Industry/Entity Type

Searchly

Coding

Coded - Design and coding required

Font styles to use
Sans Serif

Requirements
Must have
• I want this site to be fun and colorful. It still needs to be professional looking as not to deter business accounts. If you use photos, they must reflect Florida lawn. Note the architecture the homes, grass type, types of plants.
Should not have
• My current site is ok. I use it just as a

```html
<!DOCTYPE html>
<html lang="en">
<head>
<meta charset="utf-8">
<title>Verdant Row – Lawn Care</title>
<link rel="stylesheet" href="https://fonts.googleapis.com/css2?family=Mulish:wght@400;600;700&family=Varela+Round&family=Arimo:wght@400;700&display=swap">
<style>
:root{
  --green:#6bb33f;
  --green-dark:#4f9a2a;
  --orange:#e84518;
  --red:#d23b1e;
  --text-gray:#777;
  --bg-light:#f3f3f1;
  --footer:#2d2c2c;
  --footer-bottom:#222;
  --blue:#1d5fb0;
  --white:#fff;
}
*{margin:0;padding:0;box-sizing:border-box}
html,body{width:790px;height:1200px;overflow:hidden}
body{position:relative;background:var(--white);font-family:"Mulish",sans-serif;color:#333}
.abs{position:absolute}

/* header */
.site-header{left:0;top:0;width:790px;height:82px;background:var(--white)}
.brand{left:94px;top:16px;width:120px}
.brand-name{display:flex;align-items:center;gap:5px;font-family:"Varela Round",sans-serif;font-size:17px;color:var(--green-dark);line-height:1;white-space:nowrap}
.brand-name .dot{width:10px;height:10px;border-radius:50%;background:var(--red);flex:none}
.brand-meta{font-family:"Arimo",sans-serif;font-size:6px;font-weight:700;color:#111;margin-top:5px;line-height:1.3;white-space:nowrap}
.portal-btn{left:620px;top:15px;width:78px;height:23px;background:var(--blue);border-radius:3px;color:var(--white);font-size:8px;display:flex;align-items:center;justify-content:center;gap:4px}
.portal-btn .ic{width:9px;height:9px;border-radius:50%;background:#f5a623}
.main-nav{right:92px;top:54px;display:flex;gap:34px;font-size:9.5px;letter-spacing:.2px}
.main-nav a{color:#333;text-decoration:none}
.main-nav a.active{color:var(--green-dark)}

/* hero */
.hero{left:0;top:82px;width:790px;height:320px;background:linear-gradient(180deg,#6a6a60 0%,#3f5a2a 30%,#5d9a2c 62%,#4a8a22 100%)}
.hero-dots{left:379px;top:373px;display:flex;gap:4px}
.hero-dots span{width:8px;height:8px;border-radius:50%;background:var(--white)}
.hero-dots span.on{background:#d41d1d}

/* welcome */
.welcome{left:0;top:402px;width:790px;height:423px;background:var(--bg-light)}
.welcome-title{left:0;top:424px;width:790px;text-align:center;color:var(--red);font-size:11.5px;font-weight:600;letter-spacing:.3px}
.welcome-text{left:95px;top:450px;width:600px;text-align:center;color:var(--text-gray);font-size:7.4px;line-height:16.8px;white-space:nowrap}

.feature{top:524px;height:211px;width:302px}
.feature-video{left:94px;background:#000}
.feature-video .media{position:absolute;left:0;top:27px;width:100%;height:163px;background:linear-gradient(180deg,#3d3a33 0%,#4a4338 55%,#3f5a2b 100%)}
.feature-photo{left:395px;background:linear-gradient(180deg,#c9c6bd 0%,#b79a80 40%,#9a8a78 62%,#5f9a32 80%,#4c8a24 100%)}
.feature h3{position:absolute;font-family:"Varela Round",sans-serif;font-weight:400;color:var(--white);font-size:21px;white-space:nowrap}
.feature-video h3{left:0;width:100%;text-align:center;top:86px}
.feature-video p{position:absolute;left:0;width:100%;text-align:center;top:117px;color:var(--white);font-size:7.6px;font-weight:600}
.feature-photo h3{left:99px;top:78px}

.services-bar{left:94px;top:735px;width:603px;height:55px;background:var(--orange);color:var(--white)}
.services-bar h2{position:absolute;left:0;width:100%;top:14px;text-align:center;font-family:"Varela Round",sans-serif;font-weight:400;font-size:23px}
.arrow{position:absolute;top:0;width:34px;height:55px;display:flex;align-items:center;justify-content:center}
.arrow.prev{left:0;border-right:1px solid rgba(0,0,0,.15)}
.arrow.next{left:34px}

/* serve */
.serve{left:0;top:825px;width:790px;height:218px;background:var(--green)}
.serve-title{left:0;top:844px;width:790px;text-align:center;color:var(--white);font-size:13px;font-weight:600;letter-spacing:.5px}
.serve-text{left:80px;top:873px;width:630px;text-align:center;color:#eef6e4;font-size:12.4px;line-height:24px;letter-spacing:.2px;white-space:nowrap}
.serve-rule{left:94px;top:938px;width:603px;border-top:1px dashed rgba(255,255,255,.35)}
.area{top:963px;width:232px}
.area h4{font-size:11px;font-weight:600;color:var(--white);margin-bottom:7px;letter-spacing:.3px}
.area p{font-size:8.4px;line-height:15.5px;color:#d7ebc4;white-space:nowrap}
.area-icon{top:966px}

/* footer */
.site-footer{left:0;top:1043px;width:790px;height:129px;background:var(--footer)}
.foot-links{top:1057px;list-style:none}
.foot-links li{font-family:"Arimo",sans-serif;font-size:7.3px;color:#ddd;height:18.5px}
.news-title{left:402px;top:1054px;color:#eee;font-size:10px;letter-spacing:.3px}
.field{left:400px;width:130px;height:20px;background:var(--white);font-family:"Arimo",sans-serif;font-size:7.3px;color:#555;padding:5px}
.signup{left:468px;top:1138px;width:62px;height:20px;background:#444;color:#eee;font-size:10px;display:flex;align-items:center;justify-content:center}
.foot-info{left:591px;top:1056px;font-family:"Arimo",sans-serif;font-size:7.3px;color:#ddd;line-height:11px}
.social{left:591px;top:1142px;display:flex;gap:4px}
.social span{width:18px;height:18px;border-radius:50%}
.copyright{left:0;top:1172px;width:790px;height:28px;background:var(--footer-bottom);color:#ccc;font-family:"Arimo",sans-serif;font-size:7.3px;text-align:center;line-height:28px}
</style>
</head>
<body>

<header class="site-header abs">
  <div class="brand abs">
    <div class="brand-name"><span class="dot"></span>Verdant Row</div>
    <div class="brand-meta">WWW.VERDANTROW-EXAMPLE.COM<br>844-555-0142</div>
  </div>
  <div class="portal-btn abs"><span class="ic"></span>Client Portal</div>
  <nav class="main-nav abs">
    <a class="active" href="#">HOME</a>
    <a href="#">ABOUT</a>
    <a href="#">SERVICES</a>
    <a href="#">ESTIMATE</a>
    <a href="#">CONTACT US</a>
  </nav>
</header>

<section class="hero abs" role="img" aria-label="Front yard of a Florida home with a green lawn and colourful flower beds"></section>
<div class="hero-dots abs"><span class="on"></span><span></span><span></span></div>

<section class="welcome abs"></section>
<h2 class="welcome-title abs">WELCOME TO OUR COMPANY</h2>
<p class="welcome-text abs">Verdant Row is SAFE, Reliable, and Responsible. We make sure that all of our lawn care professionals are licensed, insured, drug-free, background checks<br>completed and legally eligible to work. Verdant Row offers convenient online bill pay, we accepts credit cards, and we pride ourselves with a great<br>customer service department.</p>

<div class="feature feature-video abs">
  <div class="media" role="img" aria-label="Video still of a paved driveway and garden"></div>
  <h3>Our Production</h3>
  <p>Short video about our production</p>
</div>
<div class="feature feature-photo abs" role="img" aria-label="Mediterranean-style Florida house with palms, paver driveway and red flowers">
  <h3>Lawn Care</h3>
</div>

<div class="services-bar abs">
  <div class="arrow prev"><svg width="12" height="10" viewBox="0 0 12 10"><path d="M11 5H2M5 1L1 5l4 4" stroke="#fff" stroke-width="2" fill="none"/></svg></div>
  <div class="arrow next"><svg width="12" height="10" viewBox="0 0 12 10"><path d="M1 5h9M7 1l4 4-4 4" stroke="#fff" stroke-width="2" fill="none"/></svg></div>
  <h2>Services</h2>
</div>

<section class="serve abs"></section>
<h2 class="serve-title abs">WE SERVE</h2>
<p class="serve-text abs">Verdant Row strives to be a one-stop 'Outdoor Service Provider'. If your outdoor services are not<br>let us show you the return on investment (ROI) earned by switching to Verdant Row.</p>
<div class="serve-rule abs"></div>

<svg class="area-icon abs" style="left:145px" width="21" height="18" viewBox="0 0 21 18"><rect x="0" y="0" width="21" height="13" fill="#fff"/><rect x="8" y="13" width="5" height="3" fill="#fff"/><rect x="5" y="16" width="11" height="2" fill="#fff"/></svg>
<div class="area abs" style="left:178px">
  <h4>Edgewater</h4>
  <p>If you are tired of lawn service companies that deliver<br>poor quality, never call you back,..</p>
</div>
<svg class="area-icon abs" style="left:438px" width="19" height="17" viewBox="0 0 19 17"><path d="M9.5 0L19 4.5 9.5 9 0 4.5z" fill="#fff"/><path d="M0 8l9.5 4.5L19 8M0 11.5L9.5 16 19 11.5" stroke="#fff" stroke-width="1.6" fill="none"/></svg>
<div class="area abs" style="left:471px">
  <h4>New Smyrna Beach</h4>
  <p>If you are tired of lawn service companies that deliver<br>poor quality, never call you back,..</p>
</div>

<footer class="site-footer abs"></footer>
<ul class="foot-links abs" style="left:94px"><li>Home</li><li>About</li><li>News</li><li>Services</li><li>What We Do</li><li>Contact Us</li></ul>
<ul class="foot-links abs" style="left:183px"><li>Grief &amp; Healing</li><li>Resources</li><li>Plan Now</li><li>Locations</li><li>Privacy Policy</li><li>Terms &amp; Conditions</li></ul>
<ul class="foot-links abs" style="left:291px"><li>Resources</li><li>Plan Now</li><li>Locations</li><li>Privacy Policy</li><li>Terms &amp; Conditions</li></ul>

<div class="news-title abs">NEWSLETTER SIGN UP</div>
<div class="field abs" style="top:1080px">Enter Name</div>
<div class="field abs" style="top:1108px">Enter Email Address</div>
<div class="signup abs">SIGN UP</div>

<div class="foot-info abs">Shooting Sports<br>Sed ut perspiciatis unde,sit<br>voluptatem a<br><br>Phone: 844-555-0142<br>Fax: 386-555-0177</div>
<div class="social abs">
  <span style="background:#3b5998"></span>
  <span style="background:#1da1f2"></span>
  <span style="background:#0e76a8"></span>
  <span style="background:#dd4b39"></span>
  <span style="background:#f57d00"></span>
</div>

<div class="copyright abs">Copyright Verdant Row 2014. All Rights Reserved.</div>

</body>
</html>
```